Letterhead Design Project For Australian Accounting Firm

Hi All,

We need a letterhead designed for our Australian Accounting firm based in Melbourne, Victoria. I have already got a logo and business cards designed which i will add to this brief. Please design the letterhead with reference to the logo and business cards, all three items need to match. The following information needs to be included on the letterhead:

QM Advisory Logo

Suite 4 527 Harlow Street, Brunswick VIC 3056
PO Box 749, Brunswick VIC 3056

Lena Kovarik B.Com RX
Director
0491 562 804

Bartholomew Venn B.Bus RX
Director
0436 705 219

www.qmadvisory-example.com.au

at the bottom of the letterhead in small size font there needs to be the following phrase:

Liability limited by a scheme approved under Professional Standards Legislation.

Also please try and incorporate the RX logo somewhere on the letterhead

We are looking for a sharp and modern looking letterhead design, something that incorporates the look of the business card and logo.

Thanks.

```html
<!DOCTYPE html>
<html lang="en">
<head>
<meta charset="utf-8">
<title>QM Advisory Letterhead</title>
<link href="https://fonts.googleapis.com/css2?family=Source+Sans+3:wght@400;600;700&display=swap" rel="stylesheet">
<style>
  :root {
    --ink: #111111;
    --paper: #ffffff;
    --accent-red: #d6202a;
    --rule: #222222;
  }
  html, body { margin: 0; padding: 0; overflow: hidden; background: var(--paper); }
  .letterhead {
    position: relative;
    width: 849px;
    height: 1200px;
    overflow: hidden;
    background: var(--paper);
    color: var(--ink);
    font-family: "Source Sans 3", "Myriad Pro", Arial, sans-serif;
  }
  .brand {
    position: absolute;
    left: 22px;
    top: 68px;
    width: 128px;
    height: 108px;
    display: flex;
    flex-direction: column;
    justify-content: center;
    align-items: flex-start;
    gap: 8px;
  }
  .brand-mark { width: 26px; height: 26px; background: var(--ink); }
  .brand-name {
    font-size: 25px;
    font-weight: 700;
    line-height: 1.05;
    color: var(--ink);
  }
  .brand-divider {
    position: absolute;
    left: 156px;
    top: 68px;
    width: 1.5px;
    height: 110px;
    background: var(--rule);
  }
  .tagline {
    position: absolute;
    left: 175px;
    top: 97px;
    font-size: 24px;
    line-height: 26px;
    letter-spacing: 0.2px;
    font-weight: 400;
  }
  .address {
    position: absolute;
    right: 24px;
    top: 56px;
    text-align: right;
    font-size: 17px;
    line-height: 22px;
  }
  .director {
    position: absolute;
    top: 132px;
    font-size: 16px;
    line-height: 23px;
    white-space: nowrap;
  }
  .director-name { font-weight: 700; }
  .director--left { left: 430px; }
  .director--right { right: 24px; text-align: right; }
  .contact-line { display: flex; align-items: center; gap: 12px; }
  .director--right .contact-line { justify-content: flex-end; }
  .contact-icon { width: 16px; height: 16px; display: block; }
  .director-divider {
    position: absolute;
    left: 609px;
    top: 130px;
    width: 1px;
    height: 68px;
    background: var(--rule);
  }
  .accreditation {
    position: absolute;
    left: 22px;
    top: 1116px;
    display: flex;
    align-items: center;
    gap: 14px;
  }
  .accreditation-badge {
    width: 56px;
    height: 56px;
    border-radius: 50%;
    background: var(--accent-red);
  }
  .accreditation-name {
    font-size: 18px;
    font-weight: 700;
    line-height: 19px;
  }
  .website {
    position: absolute;
    right: 24px;
    top: 1116px;
    font-size: 18px;
    letter-spacing: 0.3px;
  }
  .disclaimer-band {
    position: absolute;
    left: 190px;
    top: 1137px;
    width: 659px;
    height: 27px;
  }
  .disclaimer-band svg { position: absolute; inset: 0; }
  .disclaimer-text {
    position: absolute;
    left: 48px;
    top: 3px;
    color: var(--paper);
    font-size: 17px;
    line-height: 21px;
    white-space: nowrap;
  }
</style>
</head>
<body>
<div class="letterhead">
  <div class="brand">
    <div class="brand-mark"></div>
    <div class="brand-name">QM Advisory</div>
  </div>
  <div class="brand-divider"></div>
  <div class="tagline">TAXATION AND<br>BUSINESS SERVICES</div>

  <div class="address">
    Suite 4 527 Harlow Street, Brunswick VIC 3056<br>
    PO Box 749, Brunswick VIC 3056
  </div>

  <div class="director director--left">
    <div class="director-name">Lena Kovarik B.Com RX</div>
    <div class="director-role">Director</div>
    <div class="contact-line">
      <svg class="contact-icon" viewBox="0 0 16 16" aria-hidden="true">
        <rect x="1" y="0" width="14" height="16" rx="1.5" fill="var(--ink)"/>
        <rect x="4" y="3" width="8" height="8" fill="var(--paper)"/>
        <circle cx="8" cy="13.2" r="1" fill="var(--paper)"/>
      </svg>
      <span>0491 562 804</span>
    </div>
  </div>

  <div class="director-divider"></div>

  <div class="director director--right">
    <div class="director-name">Bartholomew Venn B.Bus RX</div>
    <div class="director-role">Director</div>
    <div class="contact-line">
      <svg class="contact-icon" viewBox="0 0 16 16" aria-hidden="true">
        <rect x="0" y="0" width="16" height="16" rx="1.5" fill="var(--ink)"/>
        <rect x="3" y="4.5" width="10" height="7" fill="var(--paper)"/>
        <polyline points="3,4.5 8,8.5 13,4.5" fill="none" stroke="var(--ink)" stroke-width="1.2"/>
      </svg>
      <span>0436 705 219</span>
    </div>
  </div>

  <div class="accreditation">
    <div class="accreditation-badge"></div>
    <div class="accreditation-name">RX<br>Accredited</div>
  </div>

  <div class="website">www.qmadvisory-example.com.au</div>

  <div class="disclaimer-band">
    <svg viewBox="0 0 659 27" preserveAspectRatio="none" aria-hidden="true">
      <polygon points="14,0 659,0 659,27 0,27" fill="var(--ink)"/>
      <polygon points="26,27 38,6 44,6 34,27" fill="var(--paper)"/>
    </svg>
    <div class="disclaimer-text">Liability limited by a scheme approved under Professional Standards Legislation.</div>
  </div>
</div>
</body>
</html>
```